New Business Card Design for Manufacturing

We are an engineering/manufacturing company that offers Advanced machining/assembly/engineering services, as well as innovative products for the heavy duty engine cooling markets.

We are looking to get a new business card designed that is clean and modern looking, but still fits the wide range of technical/skilled work we do.

- We hope to use this design as the base for other design work in new Presentations, web, and print work.

Industry/Entity Type

Engineering

Contact Information for Business Card

Our preferred color of blue is (RGB) 22/71/159 but can vary slightly from that color. Our content will be our Logo and full company name (Fabricated Tooling Works, Inc.), company address, name, job title, phone number with extension, cell number, fax number, website, and email address on the cards.
We'd like the full company name next to the logo, but we are open to other interpretations of that layout.
Preferably, we would like the back side to be clean with just our logo, and the front to contain all of the contact information.

Colors
2f74b4
0355a3
85abd2

Requirements
Must have
• - Logo, company name, needed content - We are open to interpretation beyond that.
• - Standard size business card.
• - Horizontal orientation.
• - Enough space for lengthy names / job titles (for example, a job title could read "Directory of Human Resources" or "V.P. of Governmental Affairs"). We need this to look clean, whether the title be short (CEO) or long (as described above).

```html
<!DOCTYPE html>
<html lang="en">
<head>
<meta charset="utf-8">
<title>Fabricated Tooling Works, Inc. — Business Card</title>
<link rel="stylesheet" href="https://fonts.googleapis.com/css2?family=Roboto:wght@400;500;700&family=Roboto+Condensed:wght@500&display=swap">
<style>
  :root {
    --brand-blue: #1552a3;
    --brand-blue-deep: #0f4f9f;
    --steel-gray: #7b8288;
    --text-gray: #4a4f55;
    --ink: #1d1f22;
    --paper: #f7f7f6;
    --backdrop: #e4e3e0;
    --white: #ffffff;
  }
  * { box-sizing: border-box; margin: 0; padding: 0; }
  html, body { width: 1200px; height: 960px; overflow: hidden; }
  body {
    background: var(--backdrop);
    font-family: "Roboto", Arial, sans-serif;
    position: relative;
  }
  .card {
    position: absolute;
    width: 600px;
    height: 342px;
    border-radius: 22px;
    overflow: hidden;
  }
  .card-front { left: 302px; top: 130px; background: var(--paper); }
  .card-back { left: 299px; top: 488px; background: var(--brand-blue-deep); }

  /* Front: brand lockup */
  .brand-lockup {
    position: absolute;
    left: 206px;
    top: 40px;
    width: 356px;
  }
  .brand-name {
    display: flex;
    align-items: center;
    gap: 10px;
    color: var(--brand-blue);
    font-weight: 700;
    font-size: 20px;
    line-height: 22px;
    letter-spacing: 0.2px;
    text-transform: uppercase;
  }
  .brand-square {
    width: 44px; height: 44px;
    background: var(--brand-blue);
    flex: none;
  }
  .brand-tagline {
    margin-top: 8px;
    color: var(--steel-gray);
    font-weight: 700;
    font-size: 12px;
    letter-spacing: 0.4px;
    text-transform: uppercase;
  }

  /* Front: person */
  .name-accent {
    position: absolute;
    left: 0; top: 188px;
    width: 8px; height: 28px;
    background: var(--brand-blue);
  }
  .person-name {
    position: absolute;
    left: 32px; top: 184px;
    font-family: "Roboto Condensed", "Arial Narrow", sans-serif;
    font-weight: 500;
    font-size: 25px;
    color: var(--brand-blue);
    text-transform: uppercase;
  }
  .person-title {
    position: absolute;
    left: 32px; top: 214px;
    right: 42px;
    display: flex;
    align-items: center;
    gap: 4px;
    font-size: 13px;
    color: var(--ink);
    white-space: nowrap;
  }
  .person-title::after {
    content: "";
    flex: 1;
    height: 1px;
    background: var(--text-gray);
  }

  /* Front: contact */
  .contact-list {
    position: absolute;
    left: 32px; top: 245px;
    list-style: none;
    font-size: 14px;
    color: var(--text-gray);
  }
  .contact-list li {
    display: flex;
    align-items: center;
    gap: 8px;
    height: 19.5px;
  }
  .contact-list svg { width: 13px; height: 13px; fill: var(--brand-blue); flex: none; }
  .address {
    position: absolute;
    right: 42px; top: 259px;
    text-align: right;
    font-size: 14px;
    line-height: 20px;
    color: var(--text-gray);
    font-style: normal;
  }

  /* Front: footer bands */
  .footer-bands { position: absolute; left: 0; bottom: 0; width: 600px; height: 28px; }
  .footer-url {
    position: absolute;
    right: 20px; bottom: 5px;
    color: var(--white);
    font-size: 14px;
    line-height: 16px;
    font-weight: 500;
  }

  /* Back */
  .back-lockup {
    position: absolute;
    left: 0; right: 0; top: 118px;
    text-align: center;
    color: var(--white);
  }
  .back-name {
    display: inline-flex;
    align-items: center;
    gap: 14px;
    font-weight: 700;
    font-size: 30px;
    text-transform: uppercase;
    letter-spacing: 0.3px;
  }
  .back-square { width: 34px; height: 34px; background: var(--white); flex: none; }
  .back-tagline {
    margin-top: 14px;
    font-weight: 700;
    font-size: 17px;
    letter-spacing: 0.4px;
    text-transform: uppercase;
  }
  .back-url {
    position: absolute;
    left: 0; right: 0; top: 284px;
    text-align: center;
    color: var(--white);
    font-size: 14px;
    font-weight: 500;
    letter-spacing: 2.6px;
  }
</style>
</head>
<body>
  <section class="card card-front" aria-label="Business card front">
    <div class="brand-lockup">
      <div class="brand-name"><span class="brand-square"></span><span>Fabricated Tooling<br>Works, Inc.</span></div>
      <div class="brand-tagline">Built For What's Next</div>
    </div>

    <span class="name-accent"></span>
    <h1 class="person-name">Daniel Reyes</h1>
    <p class="person-title">V.P. of Governmental Affairs</p>

    <ul class="contact-list">
      <li><svg viewBox="0 0 24 24"><path d="M6.6 10.8a15.1 15.1 0 0 0 6.6 6.6l2.2-2.2a1 1 0 0 1 1-.25 11.4 11.4 0 0 0 3.6.57 1 1 0 0 1 1 1V20a1 1 0 0 1-1 1A17 17 0 0 1 3 4a1 1 0 0 1 1-1h3.5a1 1 0 0 1 1 1c0 1.25.2 2.450.57 3.57a1 1 0 0 1-.25 1z"/></svg>555 214 7730</li>
      <li><svg viewBox="0 0 24 24"><path d="M7 1h10a2 2 0 0 1 2 2v18a2 2 0 0 1-2 2H7a2 2 0 0 1-2-2V3a2 2 0 0 1 2-2zm0 3v14h10V4zm5 15.5a1.2 1.2 0 1 0 0 2.4 1.2 1.2 0 0 0 0-2.4z"/></svg>555 389 6142</li>
      <li><svg viewBox="0 0 24 24"><path d="M2 5h20v14H2zm2 2v.5l8 5 8-5V7zm0 2.8V17h16V9.8l-8 5z"/></svg>daniel@fabricatedtoolingworks.com</li>
    </ul>

    <address class="address">2214 Cedar Bluff Drive<br>Fairbanks, Alaska 99701</address>

    <svg class="footer-bands" viewBox="0 0 600 28" aria-hidden="true">
      <path d="M0 6 H292 L286 14 H0 Z" fill="var(--steel-gray)"/>
      <path d="M0 16 H600 V28 H0 Z" fill="var(--brand-blue)"/>
      <path d="M280 16 L292 3 Q295 0 301 0 H600 V28 H280 Z" fill="var(--brand-blue)"/>
    </svg>
    <span class="footer-url">www.fabricatedtoolingworks.com</span>
  </section>

  <section class="card card-back" aria-label="Business card back">
    <div class="back-lockup">
      <div class="back-name"><span class="back-square"></span>Fabricated Tooling Works</div>
      <div class="back-tagline">Built For What's Next</div>
    </div>
    <p class="back-url">www.fabricatedtoolingworks.com</p>
  </section>
</body>
</html>
```